KM Rentals

Need a one page add for insertion in print media that can also be used as email flyer. Attached my rendition, needs improvement. Please incorporate a list of available Tooling/Equipment to include: dirt augers, rock augers, core barrels, drill buckets, clean-out buckets, slurry augers, over-cutters, under-reamers, steel casing, continuous flight augers (CFA), cranes, concrete pumps, crane-mount rigs, augercast set-ups

```html
<!DOCTYPE html>
<html lang="en">
<head>
<meta charset="utf-8">
<title>KM Rentals – Drill Tool Rentals Flyer</title>
<link href="https://fonts.googleapis.com/css2?family=Open+Sans:wght@300;400;600;700;800&display=swap" rel="stylesheet">
<style>
  :root {
    --brand-blue: #0b4ea2;
    --brand-blue-dark: #0a2f74;
    --brand-navy: #0b1f55;
    --brand-yellow: #f5d20f;
    --ink: #1b2233;
    --paper: #ffffff;
    --backdrop: #d9d9d9;
  }
  * { box-sizing: border-box; margin: 0; padding: 0; }
  html, body {
    width: 1029px; height: 1200px; overflow: hidden;
    background: var(--backdrop);
    font-family: "Open Sans", Arial, sans-serif;
  }
  .flyer {
    position: absolute; left: 50.5px; top: 0;
    width: 948px; height: 1226px;
    transform: scale(0.9788); transform-origin: top left;
    background: var(--paper); overflow: hidden;
  }
  .abs { position: absolute; }

  .hero {
    left: 0; top: 173px; width: 948px; height: 337px;
    background: linear-gradient(180deg, #0d2f86 0%, #123c9a 45%, #0a235f 80%, #162a4a 100%);
  }
  .header-shapes { left: 0; top: 0; width: 948px; height: 180px; }

  .brand-name {
    left: 82px; top: 48px;
    font-size: 66px; font-weight: 800; letter-spacing: 1px;
    color: var(--brand-blue); line-height: 1;
  }
  .brand-square {
    left: 20px; top: 58px; width: 46px; height: 46px;
    background: var(--brand-blue);
  }
  .coverage-map {
    left: 690px; top: 38px; width: 222px; height: 140px;
    background: linear-gradient(135deg, #c8202e 0%, #ffffff 50%, #1d3a8a 100%);
    border-radius: 6px;
  }

  .headline {
    left: 0; top: 266px; width: 948px; text-align: center;
    font-size: 47px; font-weight: 800; color: var(--brand-yellow);
    letter-spacing: 0.5px; line-height: 1.1;
  }
  .subline {
    left: 0; top: 324px; width: 948px; text-align: center;
    font-size: 35px; font-weight: 300; color: #fff; line-height: 1.1;
  }

  .photo { box-shadow: 0 4px 8px rgba(0,0,0,0.35); }
  .photo.tone-auger { background: linear-gradient(135deg, #a88a68, #6f5a44); }
  .photo.tone-bucket { background: linear-gradient(135deg, #e9e9e9, #9c8d7d); }
  .photo.tone-yard { background: linear-gradient(180deg, #9bb6d0 0%, #6a5038 45%, #4e3a2a 100%); }
  .photo.tone-trailer { background: linear-gradient(180deg, #8fb8e6 0%, #7a4a2e 55%, #a69a8a 100%); }

  .intro {
    left: 78px; top: 983px; width: 450px;
    font-size: 20px; font-weight: 700; color: var(--ink); line-height: 1.38;
  }
  .intro .accent { color: var(--brand-blue); }

  .list-title {
    left: 548px; top: 624px; width: 321px; height: 47px;
    background: var(--brand-blue); color: #fff;
    font-size: 25px; font-weight: 700; letter-spacing: 0.5px;
    display: flex; align-items: center; justify-content: center;
  }
  .list-title::after {
    content: ""; position: absolute; left: 152px; bottom: -9px;
    border-left: 9px solid transparent; border-right: 9px solid transparent;
    border-top: 9px solid var(--brand-blue);
  }
  .tool-list { left: 570px; top: 690px; list-style: none; }
  .tool-list li {
    display: flex; align-items: center; gap: 8px;
    height: 30.2px; font-size: 19.5px; font-weight: 600; color: var(--ink);
  }
  .tool-list svg { width: 16px; height: 16px; flex: none; }

  .footer-shapes { left: 0; top: 1090px; width: 948px; height: 136px; }
  .contact {
    left: 77px; top: 1120px;
    font-size: 20px; color: var(--ink); line-height: 28px;
  }
  .contact b { font-weight: 700; }
  .website {
    left: 570px; top: 1178px; display: flex; align-items: center; gap: 9px;
    font-size: 21px; color: #fff;
  }
  .website b { font-weight: 700; }
</style>
</head>
<body>
<main class="flyer">

  <div class="abs hero" role="img" aria-label="Drilling rig site with crane at dusk under a deep blue sky"></div>

  <svg class="abs header-shapes" viewBox="0 0 948 180" aria-hidden="true">
    <polygon points="0,0 665,0 615,173 0,173" fill="#f4f4f4"/>
    <polygon points="665,0 948,0 948,100 636,100" fill="var(--brand-yellow)"/>
    <polygon points="636,100 948,100 948,173 615,173" fill="var(--brand-blue)"/>
    <polygon points="615,173 636,100 645,100 624,173" fill="var(--brand-blue-dark)"/>
  </svg>

  <div class="abs brand-square" aria-hidden="true"></div>
  <div class="abs brand-name">KM RENTALS</div>
  <div class="abs coverage-map" role="img" aria-label="Map of the United States in flag colours marked Nationwide"></div>

  <h1 class="abs headline">YOUR DRILLING PARTNER</h1>
  <p class="abs subline">EXPERTS IN THE DRILLING INDUSTRY</p>

  <div class="abs photo tone-auger" style="left:79px;top:420px;width:243px;height:173px" role="img" aria-label="Close-up of a worn rock auger with cutting teeth"></div>
  <div class="abs photo tone-bucket" style="left:352px;top:420px;width:244px;height:173px" role="img" aria-label="Large white drill bucket beside a pickup truck"></div>
  <div class="abs photo tone-yard" style="left:625px;top:420px;width:244px;height:173px" role="img" aria-label="Equipment yard full of augers and casing"></div>

  <div class="abs photo tone-trailer" style="left:79px;top:624px;width:206px;height:146px" role="img" aria-label="Drill buckets loaded on a flatbed trailer"></div>
  <div class="abs photo tone-trailer" style="left:311px;top:624px;width:208px;height:146px" role="img" aria-label="Steel casing section on a flatbed trailer"></div>
  <div class="abs photo tone-trailer" style="left:79px;top:801px;width:206px;height:147px" role="img" aria-label="Row of augers strapped on a flatbed trailer"></div>
  <div class="abs photo tone-trailer" style="left:311px;top:801px;width:208px;height:147px" role="img" aria-label="Large flight auger on a flatbed trailer"></div>

  <p class="abs intro">Now offering a complete line of foundation drilling tools, <span class="accent">support equipment and drill rigs for RENT.</span></p>

  <h2 class="abs list-title">DRILL TOOL RENTALS</h2>
  <ul class="abs tool-list">
    <li><svg viewBox="0 0 16 16"><path d="M2 9 L6 13 L14 2" fill="none" stroke="var(--brand-blue)" stroke-width="2"/></svg>Dirt Augers</li>
    <li><svg viewBox="0 0 16 16"><path d="M2 9 L6 13 L14 2" fill="none" stroke="var(--brand-blue)" stroke-width="2"/></svg>Rock Augers</li>
    <li><svg viewBox="0 0 16 16"><path d="M2 9 L6 13 L14 2" fill="none" stroke="var(--brand-blue)" stroke-width="2"/></svg>Core Barrels</li>
    <li><svg viewBox="0 0 16 16"><path d="M2 9 L6 13 L14 2" fill="none" stroke="var(--brand-blue)" stroke-width="2"/></svg>Drill Buckets</li>
    <li><svg viewBox="0 0 16 16"><path d="M2 9 L6 13 L14 2" fill="none" stroke="var(--brand-blue)" stroke-width="2"/></svg>Clean-out Buckets</li>
    <li><svg viewBox="0 0 16 16"><path d="M2 9 L6 13 L14 2" fill="none" stroke="var(--brand-blue)" stroke-width="2"/></svg>Slurry Augers</li>
    <li><svg viewBox="0 0 16 16"><path d="M2 9 L6 13 L14 2" fill="none" stroke="var(--brand-blue)" stroke-width="2"/></svg>Over-cutters</li>
    <li><svg viewBox="0 0 16 16"><path d="M2 9 L6 13 L14 2" fill="none" stroke="var(--brand-blue)" stroke-width="2"/></svg>Under-reamers</li>
    <li><svg viewBox="0 0 16 16"><path d="M2 9 L6 13 L14 2" fill="none" stroke="var(--brand-blue)" stroke-width="2"/></svg>Steel Casing</li>
    <li><svg viewBox="0 0 16 16"><path d="M2 9 L6 13 L14 2" fill="none" stroke="var(--brand-blue)" stroke-width="2"/></svg>Continuous Flight Augers (cfa)</li>
    <li><svg viewBox="0 0 16 16"><path d="M2 9 L6 13 L14 2" fill="none" stroke="var(--brand-blue)" stroke-width="2"/></svg>Cranes</li>
    <li><svg viewBox="0 0 16 16"><path d="M2 9 L6 13 L14 2" fill="none" stroke="var(--brand-blue)" stroke-width="2"/></svg>Concrete Pumps</li>
    <li><svg viewBox="0 0 16 16"><path d="M2 9 L6 13 L14 2" fill="none" stroke="var(--brand-blue)" stroke-width="2"/></svg>Crane-mount Rigs</li>
    <li><svg viewBox="0 0 16 16"><path d="M2 9 L6 13 L14 2" fill="none" stroke="var(--brand-blue)" stroke-width="2"/></svg>Augercast Set-ups</li>
    <li><svg viewBox="0 0 16 16"><path d="M2 9 L6 13 L14 2" fill="none" stroke="var(--brand-blue)" stroke-width="2"/></svg>Complete Mud Systems</li>
  </ul>

  <svg class="abs footer-shapes" viewBox="0 0 948 136" aria-hidden="true">
    <polygon points="0,4 500,4 540,136 0,136" fill="var(--brand-yellow)"/>
    <polygon points="518,68 948,68 948,136 540,136" fill="var(--brand-blue)"/>
    <polygon points="518,68 530,68 552,136 540,136" fill="#5d8fd4"/>
  </svg>

  <address class="abs contact" style="font-style:normal">
    For Information Contact <b>RAY HOLDEN</b><br>
    MOBILE <b>(555) 014-2290</b><br>
    EMAIL <b>rholden@kmfoundationtools.com</b>
  </address>

  <div class="abs website">
    <svg width="20" height="20" viewBox="0 0 20 20" aria-hidden="true">
      <g fill="none" stroke="var(--brand-yellow)" stroke-width="1.6">
        <circle cx="10" cy="10" r="8"/>
        <ellipse cx="10" cy="10" rx="3.6" ry="8"/>
        <line x1="2" y1="10" x2="18" y2="10"/>
      </g>
    </svg>
    <span>www.<b>KMFoundationTools</b>.com</span>
  </div>

</main>
</body>
</html>
```